Brovane Grand Opening

I need a one sided flyer that advertises my grand opening for our new equipment dealership.

Grand Opening

New and Used Equipment Sales
Equipment Rentals
Residential, Commercial and Industrial Rental Equipment
Construction and Industrial Supply
Custom Metal Fabrication
Mobile Welding Service
Pickup and Delivery Service
24hr. Emergency Dedicated Service

Now Open!

4362 Marlowfield HWY
Easley, SC 29640

(555) 318 - 4026

7:00am-7:00pm Monday - Friday
8:00am-3:00pm Saturday

www.brovanegear.example

```html
<!DOCTYPE html>
<html lang="en">
<head>
<meta charset="utf-8">
<title>Brovane Grand Opening</title>
<link href="https://fonts.googleapis.com/css2?family=Teko:wght@600;700&family=Poppins:wght@400;500;600;700&display=swap" rel="stylesheet">
<style>
:root{
  --red:#e8202a;
  --black:#0d0d0d;
  --grey:#4a4a4a;
  --white:#ffffff;
  --text:#3a3a3a;
}
*{margin:0;padding:0;box-sizing:border-box}
html,body{width:931px;height:1200px;overflow:hidden;background:#dcdcdc}
.flyer{position:relative;width:931px;height:1200px;background:var(--white);font-family:"Poppins",sans-serif;overflow:hidden}
.backdrop{position:absolute;left:0;top:0}
.brand{position:absolute;top:48px;left:0;width:931px;display:flex;justify-content:center;align-items:center;gap:12px}
.brand-mark{width:26px;height:26px;background:var(--red)}
.brand-name{font-family:"Teko",sans-serif;font-weight:700;font-size:64px;line-height:1;color:var(--white);letter-spacing:1px;padding-top:8px}
.headline{position:absolute;top:550px;left:0;width:931px;text-align:center;font-family:"Teko",sans-serif;font-weight:700;font-size:146px;line-height:1;color:var(--white);letter-spacing:2px}
.address{position:absolute;top:724px;left:0;width:931px;text-align:center;color:var(--white);font-weight:500;font-size:23px}
.hours{position:absolute;top:782px;left:0;width:931px;text-align:center;font-size:23px;color:var(--white);font-weight:600}
.hours .days{font-weight:400;color:#1a1a1a}
.hours .sep{margin:0 18px;font-weight:400}
.services{position:absolute;top:824px;left:48px;width:828px;display:flex;list-style:none}
.service{flex:1;display:flex;flex-direction:column;align-items:center;border-right:1px solid #d6d6d6;height:198px}
.service:last-child{border-right:none}
.service-icon{width:86px;height:86px}
.service-label{margin-top:10px;text-align:center;font-size:16px;line-height:18px;color:var(--text)}
.badge{position:absolute;left:54px;top:1044px;width:116px;height:116px}
.emergency-label{position:absolute;left:180px;top:1068px;font-family:"Teko",sans-serif;font-weight:600;font-size:32px;line-height:1;color:var(--white);letter-spacing:0.5px}
.emergency-sub{position:absolute;left:180px;top:1101px;font-weight:500;font-size:16px;line-height:22px;color:var(--white)}
.pickup-line{position:absolute;left:404px;top:1054px;display:flex;align-items:center;gap:7px;font-weight:700;font-size:22px;line-height:30px;color:var(--red);letter-spacing:0.6px;white-space:nowrap}
.now-open{position:absolute;left:398px;top:1094px;font-family:"Teko",sans-serif;font-weight:700;font-size:58px;line-height:1;color:var(--black);font-style:italic;white-space:nowrap}
.now-open .now{color:var(--red)}
.contact{position:absolute;left:652px;top:1094px;font-weight:600;font-size:16px;line-height:22px;color:var(--text);list-style:none;white-space:nowrap}
.contact li{display:flex;align-items:center;gap:5px}
</style>
</head>
<body>
<main class="flyer">
  <svg class="backdrop" width="931" height="1200" viewBox="0 0 931 1200">
    <defs>
      <linearGradient id="redLeft" x1="0" y1="0" x2="1" y2="1">
        <stop offset="0" stop-color="#a5141d"/><stop offset="0.6" stop-color="#d81f26"/><stop offset="1" stop-color="#7a0d12"/>
      </linearGradient>
      <linearGradient id="redRight" x1="1" y1="0" x2="0" y2="1">
        <stop offset="0" stop-color="#c0161f"/><stop offset="0.5" stop-color="#e3222a"/><stop offset="1" stop-color="#8e1016"/>
      </linearGradient>
      <linearGradient id="siteTones" x1="0" y1="0" x2="0" y2="1">
        <stop offset="0" stop-color="#8aa6c4"/><stop offset="0.35" stop-color="#e6b52a"/><stop offset="0.7" stop-color="#b9a184"/><stop offset="1" stop-color="#8b7c6c"/>
      </linearGradient>
    </defs>
    <rect x="0" y="0" width="931" height="735" fill="var(--black)"/>
    <polygon points="0,47 213,47 328,521 0,521" fill="url(#redLeft)" role="img" aria-label="Photo of a row of green tractors tinted red"/>
    <polygon points="704,47 931,47 931,521 592,521" fill="url(#redRight)" role="img" aria-label="Photo of a tracked excavator on a trailer tinted red"/>
    <polygon points="248,146 672,146 576,544 367,544" fill="url(#siteTones)" role="img" aria-label="Photo of a yellow excavator digging gravel on a site"/>
    <rect x="0" y="735" width="931" height="131" fill="var(--red)"/>
    <polygon points="180,700 756,700 728,766 208,766" fill="var(--grey)"/>
    <circle cx="468" cy="697" r="24" fill="var(--red)" stroke="var(--white)" stroke-width="3"/>
    <path d="M468 684a8 8 0 0 0-8 8c0 6 8 14 8 14s8-8 8-14a8 8 0 0 0-8-8z" fill="var(--white)"/>
    <circle cx="468" cy="692" r="3" fill="var(--red)"/>
    <polygon points="162,1066 322,1066 340,1098 162,1098" fill="var(--red)"/>
    <polygon points="158,1098 380,1098 362,1128 158,1128" fill="var(--grey)"/>
  </svg>

  <header class="brand">
    <span class="brand-mark"></span>
    <span class="brand-name">BROVANE</span>
  </header>

  <h1 class="headline">GRAND OPENING</h1>
  <p class="address">4362 Marlowfield HWY Easley, SC 29640</p>
  <p class="hours">7:00am-7:00pm <span class="days">Monday - Friday</span><span class="sep">|</span>8:00am-3:00pm <span class="days">Saturday</span></p>

  <ul class="services">
    <li class="service">
      <svg class="service-icon" viewBox="0 0 86 86"><circle cx="43" cy="46" r="40" fill="#ccc"/><circle cx="43" cy="43" r="38" fill="var(--red)"/><circle cx="43" cy="43" r="31" fill="var(--grey)"/><circle cx="41" cy="41" r="11" fill="none" stroke="#fff" stroke-width="4" stroke-dasharray="5 3"/><circle cx="41" cy="41" r="4" fill="#fff"/><line x1="48" y1="48" x2="56" y2="56" stroke="#fff" stroke-width="4"/></svg>
      <span class="service-label">New and<br>Used<br>Equipment<br>Sales</span>
    </li>
    <li class="service">
      <svg class="service-icon" viewBox="0 0 86 86"><circle cx="43" cy="46" r="40" fill="#ccc"/><circle cx="43" cy="43" r="38" fill="var(--red)"/><circle cx="43" cy="43" r="31" fill="var(--grey)"/><line x1="30" y1="30" x2="56" y2="56" stroke="#fff" stroke-width="5"/><line x1="56" y1="30" x2="30" y2="56" stroke="#fff" stroke-width="5"/><circle cx="29" cy="29" r="5" fill="#fff"/><circle cx="57" cy="29" r="5" fill="#fff"/></svg>
      <span class="service-label">Equipment<br>Rentals</span>
    </li>
    <li class="service">
      <svg class="service-icon" viewBox="0 0 86 86"><circle cx="43" cy="46" r="40" fill="#ccc"/><circle cx="43" cy="43" r="38" fill="var(--red)"/><circle cx="43" cy="43" r="31" fill="var(--grey)"/><rect x="33" y="26" width="12" height="32" fill="#fff"/><rect x="46" y="38" width="9" height="20" fill="#fff"/><rect x="27" y="58" width="32" height="3" fill="#fff"/></svg>
      <span class="service-label">Residential,<br>Commercial<br>&amp; Industrial<br>Rental<br>Equipment</span>
    </li>
    <li class="service">
      <svg class="service-icon" viewBox="0 0 86 86"><circle cx="43" cy="46" r="40" fill="#ccc"/><circle cx="43" cy="43" r="38" fill="var(--red)"/><circle cx="43" cy="43" r="31" fill="var(--grey)"/><rect x="29" y="26" width="28" height="4" fill="#fff"/><rect x="31" y="30" width="4" height="28" fill="#fff"/><rect x="40" y="40" width="16" height="18" fill="#fff"/><rect x="27" y="58" width="32" height="3" fill="#fff"/></svg>
      <span class="service-label">Construction<br>&amp; Industrial<br>Supply</span>
    </li>
    <li class="service">
      <svg class="service-icon" viewBox="0 0 86 86"><circle cx="43" cy="46" r="40" fill="#ccc"/><circle cx="43" cy="43" r="38" fill="var(--red)"/><circle cx="43" cy="43" r="31" fill="var(--grey)"/><rect x="30" y="52" width="26" height="6" fill="#fff"/><line x1="38" y1="50" x2="54" y2="30" stroke="#fff" stroke-width="5"/><circle cx="36" cy="48" r="3" fill="#fff"/></svg>
      <span class="service-label">Custom<br>Metal<br>Fabrication</span>
    </li>
    <li class="service">
      <svg class="service-icon" viewBox="0 0 86 86"><circle cx="43" cy="46" r="40" fill="#ccc"/><circle cx="43" cy="43" r="38" fill="var(--red)"/><circle cx="43" cy="43" r="31" fill="var(--grey)"/><rect x="28" y="28" width="18" height="22" rx="3" fill="#fff"/><line x1="42" y1="58" x2="58" y2="36" stroke="#fff" stroke-width="4"/></svg>
      <span class="service-label">Mobile<br>Welding<br>Service</span>
    </li>
  </ul>

  <svg class="badge" viewBox="0 0 116 116">
    <circle cx="58" cy="62" r="54" fill="#e6e6e6"/>
    <circle cx="58" cy="58" r="52" fill="#fff"/>
    <circle cx="58" cy="58" r="42" fill="none" stroke="var(--red)" stroke-width="5" stroke-dasharray="190 74"/>
    <path d="M88 22l8-4-2 10z" fill="var(--red)"/>
    <text x="58" y="67" text-anchor="middle" font-family="Poppins, sans-serif" font-weight="700" font-size="26" fill="#222">24/7</text>
  </svg>
  <span class="emergency-label">EMERGENCY</span>
  <span class="emergency-sub">Dedicated Service</span>

  <div class="pickup-line">
    <svg width="40" height="24" viewBox="0 0 44 26"><rect x="8" y="2" width="22" height="16" fill="var(--grey)"/><path d="M30 7h8l5 6v5H30z" fill="var(--grey)"/><circle cx="15" cy="21" r="4" fill="var(--grey)"/><circle cx="36" cy="21" r="4" fill="var(--grey)"/><rect x="0" y="6" width="6" height="2" fill="var(--grey)"/><rect x="2" y="11" width="4" height="2" fill="var(--grey)"/></svg>
    PICKUP &amp; DELIVERY SERVICE
  </div>
  <p class="now-open"><span class="now">NOW</span> OPEN!</p>
  <ul class="contact">
    <li><svg width="12" height="12" viewBox="0 0 12 12"><path d="M2 1l3 0 1 3-2 1c1 2 2 3 3 3l1-2 3 1 0 3c-5 1-10-4-9-9z" fill="var(--red)"/></svg>(555) 318 - 4026</li>
    <li><svg width="12" height="12" viewBox="0 0 12 12"><circle cx="6" cy="6" r="5" fill="none" stroke="var(--red)" stroke-width="1.5"/><line x1="1" y1="6" x2="11" y2="6" stroke="var(--red)"/><ellipse cx="6" cy="6" rx="2" ry="5" fill="none" stroke="var(--red)"/></svg>www.brovanegear.example</li>
  </ul>
</main>
</body>
</html>
```